Legal Information Website

We need a website that will serve as a source of information for people visiting, living, and working in the United Arab Emirates, where they can go and read about legal issues, laws, crimes, and most important find legal advice and find lawyers. The following are the pages of the website:

Find a Lawyer (Home Page)
This main feature of this page should be "Find a Lawyer"
Find a Lawyer should include the searching option by practice, by lawyer’s name, by law firm name or by location.

Ask a lawyer
This function allows the user to ask a lawyer a legal question and get an answer directly from a lawyer.

Research a legal matter
This function allows the user to do research on a certain legal topic. He/she can select from different legal topics.

Contact Us:
This page should include our contact details for the visitors in case they need any assistance. Contact us by Phone, Email, or Chat.

Once the design is approved, we will provide the rest of the website text.

Target Market(s)

General Public who seek legal advice

Industry/Entity Type

Law Firm

Font styles to use
Serif
Sans Serif

Requirements
Must have
• A tool to search for lawyer's, and then display the lawyer's picture and profile and credentials.

```html
<!DOCTYPE html>
<html lang="en">
<head>
<meta charset="utf-8">
<title>Juris Harbor — Find a Lawyer</title>
<link href="https://fonts.googleapis.com/css2?family=Open+Sans:wght@300;400;600&family=Raleway:wght@300;400;500&display=swap" rel="stylesheet">
<style>
:root{
  --blue:#0da5ec;
  --logo-blue:#1b86c8;
  --navy:#124a8f;
  --dark:#2d2d2d;
  --text:#3a3a3a;
  --muted:#7a7a7a;
  --red:#c8102e;
  --line:#e3e3e3;
  --panel:#f6f5f3;
  --caption:#e4e4e4;
}
*{margin:0;padding:0;box-sizing:border-box}
html,body{width:968px;height:1200px;overflow:hidden;background:#fff}
body{position:relative;font-family:"Open Sans",sans-serif;color:var(--text)}
.abs{position:absolute}
a{color:inherit;text-decoration:none}

/* header */
.brand{left:89px;top:38px;display:flex;align-items:center;gap:10px}
.brand-mark{width:40px;height:40px;border-radius:50%;background:var(--logo-blue)}
.brand-name{font-family:"Raleway",sans-serif;font-weight:400;font-size:30px;color:var(--logo-blue);line-height:1}
.brand-tag{left:185px;top:87px;font-size:10.5px;color:#555}
.social-label{left:672px;top:46px;font-size:9.5px;color:var(--muted);letter-spacing:.2px}
.social{top:39px;width:26px;height:26px;border-radius:50%}
.s1{left:785px;background:#1da1e2}.s2{left:818px;background:#d8403c}.s3{left:851px;background:#4d73a8}
.crumbs{left:443px;top:84px;font-size:9.5px;color:var(--muted);display:flex;gap:6px}
.crumbs span.sep{color:#aaa}
.search{left:720px;top:77px;width:156px;height:24px;border:1px solid #d6d6d6;border-radius:12px;font-size:9.5px;color:#888;padding:5px 12px}
.search svg{position:absolute;right:9px;top:5px}

/* nav */
.nav{left:0;top:133px;width:968px;height:40px;background:var(--dark);display:flex;align-items:center;padding-left:90px;font-size:10.5px;color:#fff;letter-spacing:.3px}
.nav .dot{margin:0 12px;font-size:8px}

/* hero */
.hero{left:0;top:173px;width:968px;height:417px;border-bottom:2px solid #ececec}
.hero-kicker{left:89px;top:130px;font-family:"Raleway",sans-serif;font-weight:500;font-size:17px;color:#222}
.hero-title{left:88px;top:156px;font-family:"Raleway",sans-serif;font-weight:300;font-size:44px;color:#222;letter-spacing:-.3px}
.hero-text{left:90px;top:216px;font-family:"Raleway",sans-serif;font-weight:300;font-size:18px;line-height:24px;color:#222;width:420px}
.btn-discover{left:90px;top:276px;width:185px;height:44px;border-radius:4px;background:var(--blue);color:#fff;font-family:"Raleway",sans-serif;font-weight:500;font-size:17px;display:flex;align-items:center;padding-left:14px;gap:9px}
.dots{display:flex;gap:6px}
.dots i{display:block;width:8px;height:8px;border-radius:50%}
.hero-dots{left:92px;top:337px}
.hero-dots i{background:var(--blue)}.hero-dots i.on{background:#222;width:10px;height:10px;margin-top:-1px}
.hero-visual{left:512px;top:93px;width:444px;height:323px;background:radial-gradient(ellipse at 60% 60%,#e9dcc4 0%,#c9a56a 35%,#8a3a22 55%,#fff 78%)}

/* welcome */
.h2{font-weight:300;font-size:17px;color:#333}
.welcome-h{left:94px;top:624px}
.welcome-p{left:94px;top:666px;width:312px;font-size:10.3px;line-height:19.4px;color:#444}
.welcome-p .lnk{color:#3b6aa8}
.learn{left:95px;top:758px;font-size:9.5px;font-weight:600;color:var(--red)}
.small-dots{gap:4px}
.small-dots i{width:7px;height:7px;background:#d2d2d2}
.small-dots i.on{background:#fff;border:1px solid #bbb}
.welcome-dots{left:97px;top:790px}
.card{top:641px;width:144px;height:154px}
.card .photo{height:115px}
.card .cap{height:39px;background:var(--caption);border-bottom:2px solid #333;font-size:13px;color:#444;text-align:center;line-height:37px}
.c1{left:412px}.c1 .photo{background:linear-gradient(160deg,#e4b45a,#9a5a1e)}
.c2{left:573px}.c2 .photo{background:linear-gradient(160deg,#b8b8b8,#3a3a3a)}
.c3{left:733px}.c3 .photo{background:linear-gradient(160deg,#cfcfcf,#2e2e2e)}

/* lawyers */
.lawyers-h{left:91px;top:833px}
.lawyer-photo{left:85px;top:871px;width:137px;height:202px;background:linear-gradient(180deg,#d8c0a8 0%,#5b6570 35%,#3b4450 100%);border-radius:60px 60px 6px 6px}
.lawyer-name{left:253px;top:897px;font-size:14px;color:var(--red)}
.lawyer-role{left:253px;top:919px;font-size:10px;color:var(--red)}
.lawyer-addr{left:253px;top:935px;font-size:7.5px;color:#777}
.lawyer-bio{left:252px;top:953px;width:405px;font-size:10px;line-height:15.5px;color:var(--muted)}
.lawyer-dots{left:252px;top:1014px}

/* search panel */
.search-h{left:682px;top:842px}
.finder{left:682px;top:877px;width:194px;height:236px;background:var(--panel);border:1px solid var(--line);border-radius:3px}
.finder-intro{left:9px;top:8px;width:176px;font-size:10.3px;line-height:15px;color:#555;padding-bottom:6px;border-bottom:1px solid #e1e1e1}
.f-label{left:9px;font-size:10.3px;color:#555}
.f-input{left:10px;width:173px;height:22px;background:#fff;border:1px solid #ececec;font-size:8.5px;font-style:italic;color:#999;padding:5px 7px}
.btn-find{left:12px;top:197px;width:95px;height:28px;background:var(--navy);border-radius:3px;color:#fff;font-size:10.5px;font-weight:600;text-align:center;line-height:28px}

/* footer */
.footer{left:0;top:1158px;width:968px;height:42px;background:var(--dark);color:#fff;font-size:10px;text-align:center;line-height:42px}
</style>
</head>
<body>

<header>
  <div class="abs brand"><span class="brand-mark"></span><span class="brand-name">Juris Harbor</span></div>
  <div class="abs brand-tag">Briefly Speaking, We're the Best.</div>
  <div class="abs social-label">SOCIALIZE WITH US :</div>
  <span class="abs social s1" aria-label="Social link"></span>
  <span class="abs social s2" aria-label="Social link"></span>
  <span class="abs social s3" aria-label="Social link"></span>
  <nav class="abs crumbs"><a>REPERTOIRE DO PERSONAL</a><span class="sep">›</span><a>BLOGUE</a><span class="sep">›</span><a>SALLE DE PARSE</a></nav>
  <div class="abs search">SEARCH...
    <svg width="11" height="11" viewBox="0 0 11 11"><circle cx="4.5" cy="4.5" r="3.5" fill="none" stroke="#aaa" stroke-width="1.4"/><line x1="7" y1="7" x2="10" y2="10" stroke="#aaa" stroke-width="1.6"/></svg>
  </div>
</header>

<nav class="abs nav">
  <a>HOME</a><span class="dot">•</span><a>FIND A LAWYER</a><span class="dot">•</span><a>KNOW YOUR RIGHTS</a><span class="dot">•</span><a>CHECK THE NEWS</a><span class="dot">•</span><a>READ ARTICLES</a><span class="dot">•</span><a>CONTACT US</a>
</nav>

<section class="abs hero">
  <div class="abs hero-kicker">Breifly Speaking</div>
  <h1 class="abs hero-title" style="font-weight:300">The Juris Harbor</h1>
  <p class="abs hero-text">Sed ut perspiciatis unde omnis iste natus error sit voluptatem accusantium doloremque laudantium.</p>
  <a class="abs btn-discover">
    <svg width="22" height="22" viewBox="0 0 22 22"><circle cx="11" cy="11" r="9.5" fill="none" stroke="#fff" stroke-width="2"/><path d="M6.5 11.2l3 3 6-6" fill="none" stroke="#fff" stroke-width="2"/></svg>
    Discover More</a>
  <div class="abs dots hero-dots"><i></i><i></i><i class="on"></i></div>
  <div class="abs hero-visual" role="img" aria-label="Brass scales of justice and a wooden gavel resting on law books"></div>
</section>

<section>
  <h2 class="abs h2 welcome-h">Welcome to the Juris Harbor</h2>
  <p class="abs welcome-p">Lorem ipsum dolor sit amet, consectetur adipiscing elit. Mauris sit amet enim mauris, ac fermentum felis. Nam sit amet massa velit, <span class="lnk">adipiscing</span> dapibus velit. Nulla facilisi. Curabitur id libero est, non sollicitudin lectus. Pellentesque habitant</p>
  <a class="abs learn">LEARN MORE ›</a>
  <div class="abs dots small-dots welcome-dots"><i></i><i></i><i class="on"></i></div>

  <article class="abs card c1"><div class="photo" role="img" aria-label="Lawyer addressing a courtroom"></div><div class="cap">Real Estate Abatement</div></article>
  <article class="abs card c2"><div class="photo" role="img" aria-label="Smiling legal professional with colleagues"></div><div class="cap">Alimony Reform Act</div></article>
  <article class="abs card c3"><div class="photo" role="img" aria-label="Statue of justice in front of law books"></div><div class="cap">Immigration Reform</div></article>
</section>

<section>
  <h2 class="abs h2 lawyers-h">Our Lawyers</h2>
  <div class="abs lawyer-photo" role="img" aria-label="Portrait of a lawyer in a grey suit with arms crossed"></div>
  <div class="abs lawyer-name">Adam Reeve</div>
  <div class="abs lawyer-role">Sit ameet dolor lipsum</div>
  <div class="abs lawyer-addr">22-Elm Lane.</div>
  <p class="abs lawyer-bio">Plusieurs variations de Lorem Ipsum peuvent être trouvées ici ou là, mais la majeure partie d'entre elles a été altérée par l'addition d'humour ou de mots aléatoires qui ne ressemblent pas une seconde à du texte standard.</p>
  <div class="abs dots small-dots lawyer-dots"><i></i><i></i><i class="on"></i></div>
</section>

<section>
  <h2 class="abs h2 search-h">Search For the Lawyer</h2>
  <form class="abs finder">
    <p class="abs finder-intro">Lorem ipsum dolor sit amet, consect-etur adipiscing elit..</p>
    <label class="abs f-label" style="top:68px">Lawyer's Name :</label>
    <div class="abs f-input" style="top:67px;margin-top:0;top:66px">enter here...</div>
    <label class="abs f-label" style="top:100px"></label>
    <label class="abs f-label" style="top:101px">Law Firm Name :</label>
    <div class="abs f-input" style="top:114px">enter here...</div>
    <label class="abs f-label" style="top:149px">Location :</label>
    <div class="abs f-input" style="top:162px">enter here...</div>
    <div class="abs btn-find">Find Now</div>
  </form>
</section>

<footer class="abs footer">© 2014 JurisHarbor. All Rights Reserved.</footer>

</body>
</html>
```